Project Management Book Cover Design Project

The book title is:

Wendo's Manual for Hands-On Venture Steering

Subtitle:
Tips and advice on Getting it Done, even when other people think you can't!

Author name: Dorian K Whitby, BSc, PMP

The book includes some articles from my blog, www.wendosnook.example as well as new content. Feel free to read the blog for a sense of my writing style to reflect in the cover.

The book is written in a conversational style and incorporates stories to convey much of the information. All of the chapters are designed around the practical approach to doing various aspects of the project management role, without getting hung up on the specifics of a particular methodology.

The book is designed to be a useful guide to new project managers, and a well-needed break and refresher for experienced project managers.

The common thread of the book is about project management as a journey, and incorporates many travel metaphors - cars, planes, deserts, and scenic destinations.

I want the cover to be eye catching, a little serious but also fun - the cover should include a number of the travel elements and a Gantt chart (will attach picture) - perhaps "explorer" type, all laid out on a map with a small globe, compass, notebook and pen, the Gantt chart, small pocket umbrella (closed) and perhaps some scattered photos. Oh, and if it fits, a laptop or tablet. It might get cluttered but pehaps a small toy car (i.e. Tinywheel/ZipRollers) and/or airplane in the background/back edge - see how it goes.

Thanks!
Dorian Whitby

08/07/2012 Update

I am thinking of a mostly white cover with an old fashioned suitcase (open), with the key objects laying in or sticking out of the suitcase - umbrella, compass, globe, laptop, project plan pages. Back cover mostly white with a few photos scattered around the edges. More photos uploaded and replaced original photos with higher resolution versions.

Final image needs to be suitable for 300dpi and my original photos were not (had been scaled).

Possibly a multiple-direction (picket) signpost standing at he left side of the suitcase, extending up towards the title, with project management terms such as "Scope" "Requirements" "Quality" "Change" "Planning" "Cost" "Project Kickoff" "Plan" etc.

Thanks Dorian

Target Market(s)

Project Managers, managers and project team members. Both genders, Age range 18-60.

Industry/Entity Type

Travel

Requirements
Must have
• Must be suitable for 6"x9" book size

Front cover, spine and back cover elements

```html
<!DOCTYPE html>
<html lang="en">
<head>
<meta charset="utf-8">
<title>Wendo's Manual for Hands-On Venture Steering – Cover Spread</title>
<link href="https://fonts.googleapis.com/css2?family=Tinos:wght@400;700&family=Arimo:wght@400;700&display=swap" rel="stylesheet">
<style>
  :root {
    --page: #ffffff;
    --mat: #6f6a4b;
    --back-paper: #f8f0b0;
    --front-paper: #fbfbca;
    --ink: #111111;
    --spine-paper: #ffffff;
    --photo-edge: #ffffff;
  }
  * { box-sizing: border-box; margin: 0; padding: 0; }
  html, body { width: 1200px; height: 900px; overflow: hidden; background: var(--page); }
  .canvas { position: relative; width: 1200px; height: 900px; }

  .mat { position: absolute; left: 104px; top: 60px; width: 1040px; height: 722px; background: var(--mat); }

  /* Back cover */
  .back-cover {
    position: absolute; left: 176px; top: 138px; width: 404px; height: 636px;
    background: var(--back-paper); overflow: hidden;
    font-family: "Arimo", Arial, sans-serif; color: var(--ink);
  }
  .blurb { position: absolute; left: 40px; top: 36px; width: 340px; font-size: 10px; line-height: 13px; }
  .blurb p { margin-bottom: 10px; }
  .blurb ul { margin: 0 0 10px 24px; }
  .blurb li { margin-bottom: 2px; }
  .site { position: absolute; left: 22px; bottom: 30px; font-size: 13px; }

  .photo {
    position: absolute; border: 3px solid var(--photo-edge);
    box-shadow: 1px 1px 3px rgba(0,0,0,.35);
  }
  .photo--coast { background: linear-gradient(180deg, #9fc3e6 0%, #c9dbe8 45%, #7f9a8a 70%, #c7b38a 100%); }
  .photo--bay { background: linear-gradient(180deg, #7eaad8 0%, #b9d2ea 40%, #3f6f96 70%, #a99a74 100%); }
  .photo--hills { background: linear-gradient(180deg, #a8c6e4 0%, #d6e2ea 40%, #8f9a6c 65%, #6f7b54 100%); }

  /* Spine */
  .spine {
    position: absolute; left: 580px; top: 138px; width: 84px; height: 636px;
    background: var(--spine-paper); border: 3px solid var(--ink);
    display: flex; align-items: center; justify-content: center;
  }
  .spine-band {
    height: 100%; width: 46px; border-left: 2px solid var(--ink); border-right: 2px solid var(--ink);
    display: flex; align-items: center; justify-content: center;
  }
  .spine-title {
    writing-mode: vertical-rl; font-family: "Tinos", "Times New Roman", serif;
    font-variant: small-caps; font-size: 17px; white-space: nowrap; color: var(--ink);
  }

  /* Front cover */
  .front-cover {
    position: absolute; left: 664px; top: 138px; width: 478px; height: 636px;
    background: var(--front-paper); border: 2px solid #333;
    font-family: "Tinos", "Times New Roman", serif; color: var(--ink); text-align: center;
  }
  .title { position: absolute; top: 24px; left: 0; width: 100%; font-weight: 400;
    font-variant: small-caps; font-size: 36px; line-height: 42px; }
  .umbrella {
    position: absolute; left: 80px; top: 180px; width: 270px; height: 24px; border-radius: 12px;
    background: linear-gradient(180deg, #3a3a3a, #0d0d0d); transform: rotate(-8deg);
  }
  .subtitle { position: absolute; top: 252px; left: 0; width: 100%; font-size: 25px; line-height: 40px; }
  .subtitle u { text-underline-offset: 3px; }
  .planner {
    position: absolute; left: 70px; top: 370px; width: 240px; height: 140px; border-radius: 8px;
    background: linear-gradient(135deg, #2b2622, #0f0d0c 60%, #3a332b); transform: rotate(3deg);
  }
  .author { position: absolute; top: 536px; left: 0; width: 100%; font-size: 27px; }
</style>
</head>
<body>
<div class="canvas">
  <div class="mat"></div>

  <section class="back-cover">
    <div class="blurb">
      <p><b>Life is complicated.</b> You can simplify the art of getting things done, better than you usually see. This is particularly important in managing projects. In this book, Dorian Whitby shares the stories and lessons of twenty years in the field, covering practical ideas, tools and habits that work in Project Management and in everyday life.</p>
      <p>From the first kickoff to the final review, each chapter is a short journey with a clear destination, told in a friendly style with real examples from teams across many industries.</p>
      <p>What you will find in this book:</p>
      <ul>
        <li>Learn about the importance of the <b>Project Kickoff</b> – and why you need a <b>Working</b> to help you through it</li>
        <li>How to create a new <b>Project Plan</b> that actually gets used and is based on lessons learned</li>
        <li><b>Writing requirements</b> that people read and understand</li>
        <li>Keeping stakeholders informed without drowning in meetings</li>
        <li>You can't get there from here: tips on getting things done</li>
        <li>A helpful theory on the <b>value of writing</b> – and why it matters more than you expect</li>
        <li><b>Working with Virtual Teams</b> and distributed groups</li>
        <li>And much more besides</li>
      </ul>
      <p>From managing small projects to multi-million dollar programs, this is the real advice of many years and lessons learned to help you in your own career.</p>
    </div>

    <div class="photo photo--coast" role="img" aria-label="Travel photo of a coastline" style="left:20px;top:60px;width:130px;height:95px;transform:rotate(-18deg)"></div>
    <div class="photo photo--bay" role="img" aria-label="Travel photo of a bay" style="left:140px;top:66px;width:110px;height:80px;transform:rotate(8deg)"></div>
    <div class="photo photo--bay" role="img" aria-label="Travel photo of a river estuary" style="left:16px;top:210px;width:140px;height:100px;transform:rotate(-12deg)"></div>
    <div class="photo photo--hills" role="img" aria-label="Travel photo of green hills" style="left:150px;top:250px;width:120px;height:85px;transform:rotate(5deg)"></div>
    <div class="photo photo--coast" role="img" aria-label="Travel photo of a beach" style="left:16px;top:400px;width:90px;height:80px;transform:rotate(-10deg)"></div>
    <div class="photo photo--hills" role="img" aria-label="Travel photo of a scenic road" style="left:80px;top:420px;width:140px;height:95px;transform:rotate(8deg)"></div>

    <div class="site">www.wendosguides.example</div>
  </section>

  <section class="spine">
    <div class="spine-band">
      <span class="spine-title">Wendo's Manual for Hands-On Venture Steering &nbsp;–&nbsp; Dorian K Whitby, PMP</span>
    </div>
  </section>

  <section class="front-cover">
    <h1 class="title">Wendo's Manual for<br>Hands-On Venture<br>Steering</h1>
    <div class="umbrella" role="img" aria-label="Closed black pocket umbrella"></div>
    <p class="subtitle">Tips and advice on<br><u>Getting It Done</u>, even when others<br>think you can't!</p>
    <div class="planner" role="img" aria-label="Open leather planner with a pen"></div>
    <p class="author">DORIAN K WHITBY, PMP</p>
  </section>
</div>
</body>
</html>
```